Business card design for Velvet Harbor

We need business cards designed for our new marketing consulting company, Velvet Harbor. Our services include marketing strategy, go-to-market and launch planning, growth strategy, and execution. We serve medical technology and health technology companies, from startups to well-established growth companies.

The business cards should feel professional, credible, reliable and trustworthy, and should instill confidence. Also bold, creative, and modern.

The design must use the Velvet Harbor logo.

The primary brand color is this orange: #FF5501
A secondary color that you can use is this gray: #282B2D
I would prefer only to use the orange and gray. But if you feel you really need an additional accent color (please use it very sparingly, as little as possible), you can use this blue for small accent purposes: #009FED

Attached are the logo files. The main logo is the one with a little bit of orange on the left and the rest is gray.

The business card should include the following:

Velvet Harbor logo
First name and last name
Title
Email address
Phone number and type (in whatever order looks best for the design
Website (the website does not need to be in the same block as the personal info)

For example:

Nessa Pryle
Founder & Principal
nessa@velvetharbor.com
+1.628.309.4156 mobile (can use "." or spaces in between blocks of numbers)
velvetharbor.com (somewhere on the card, it does not need to be with the personal info; and note that there is no "www." at the beginning)

Note that there will be no address listed on the business card.

Target Market(s)

Executives (CEO, head of marketing, head of sales) at medical technology and health technology companies, mostly in their 40s and older, well-educated, often with advanced degrees. They are strategic thinkers, responsible for budgets, and familiar with P&L. Their comfort with and trust in using outside consultants varies.

Industry/Entity Type

Medical technology and health technology companies.

Contact Information for Business Card

See project description

Font styles to use
Sans Serif

Requirements
Must have
• Logo and see Business card details section above.

```html
<!DOCTYPE html>
<html lang="en">
<head>
<meta charset="utf-8">
<title>Velvet Harbor — Business Card</title>
<link rel="stylesheet" href="https://fonts.googleapis.com/css2?family=Montserrat:wght@300;400;500;700&display=swap">
<style>
  :root {
    --orange: #ff5501;
    --charcoal: #232629;
    --white: #ffffff;
    --page: #ffffff;
    --photo-light: #29b8f5;
    --photo-deep: #0a7fd6;
  }
  * { box-sizing: border-box; margin: 0; padding: 0; }
  html, body {
    width: 933px; height: 1200px; overflow: hidden;
    background: var(--page);
    font-family: "Montserrat", sans-serif;
  }
  .sheet { position: relative; width: 933px; height: 1200px; }

  .card {
    position: absolute; left: 24px; width: 881px; height: 516px;
    background: var(--orange); overflow: hidden;
  }
  .card--front { top: 33px; }
  .card--back { top: 657px; }

  /* Wordmark */
  .wordmark {
    display: flex; align-items: center; gap: 26px;
    color: var(--white); font-weight: 500;
    letter-spacing: 0.22em; text-transform: uppercase;
  }
  .wordmark__dot {
    border-radius: 50%; background: var(--white); flex: none;
  }
  .wordmark__text { line-height: 1.18; }
  .card--front .wordmark {
    position: absolute; left: 190px; top: 200px;
    font-size: 40px;
  }
  .card--front .wordmark__dot { width: 26px; height: 26px; }

  /* Back */
  .back__panel { position: absolute; inset: 0; width: 100%; height: 100%; }
  .back__wordmark {
    position: absolute; left: 172px; top: 490px;
    transform: rotate(-90deg); transform-origin: left top;
    font-size: 31px;
  }
  .back__wordmark .wordmark__dot { width: 20px; height: 20px; }

  .profile__photo {
    position: absolute; left: 483px; top: 124px;
    width: 117px; height: 117px; border-radius: 50%;
    border: 3px solid var(--white);
    background: radial-gradient(circle at 40% 35%, var(--photo-light), var(--photo-deep));
  }
  .profile__name {
    position: absolute; left: 619px; top: 162px;
    color: var(--white); font-weight: 700; font-size: 25px; line-height: 1;
  }
  .profile__title {
    position: absolute; left: 619px; top: 193px;
    color: var(--white); font-weight: 300; font-size: 19px; line-height: 1;
  }

  .contact {
    position: absolute; left: 389px; top: 287px;
    width: 427px; height: 189px; border-radius: 30px;
    background: var(--charcoal);
    padding: 28px 0 0 64px;
    list-style: none;
  }
  .contact__item {
    display: flex; align-items: center; gap: 13px;
    height: 34px; margin-bottom: 13px;
    color: var(--white); font-size: 18.5px; font-weight: 400;
  }
  .contact__icon {
    width: 33px; height: 33px; border-radius: 8px;
    background: var(--orange);
    display: flex; align-items: center; justify-content: center; flex: none;
  }
  .contact__icon svg { width: 19px; height: 19px; }
</style>
</head>
<body>
<main class="sheet">

  <section class="card card--front" aria-label="Card front">
    <div class="wordmark">
      <span class="wordmark__dot"></span>
      <span class="wordmark__text">Velvet<br>Harbor</span>
    </div>
  </section>

  <section class="card card--back" aria-label="Card back">
    <svg class="back__panel" viewBox="0 0 881 516" preserveAspectRatio="none" aria-hidden="true">
      <polygon points="0,0 331,0 213,516 0,516" fill="var(--charcoal)"/>
    </svg>

    <div class="wordmark back__wordmark">
      <span class="wordmark__dot"></span>
      <span class="wordmark__text">Velvet<br>Harbor</span>
    </div>

    <div class="profile__photo" role="img" aria-label="Portrait photo of Nessa Pryle"></div>
    <p class="profile__name">Nessa Pryle</p>
    <p class="profile__title">Founder &amp; Principal</p>

    <ul class="contact">
      <li class="contact__item">
        <span class="contact__icon">
          <svg viewBox="0 0 20 20" aria-hidden="true">
            <rect x="2" y="4" width="16" height="12" rx="1.5" fill="var(--white)"/>
            <path d="M2.8 5 L10 11 L17.2 5" fill="none" stroke="var(--orange)" stroke-width="1.6"/>
          </svg>
        </span>
        nessa@velvetharbor.com
      </li>
      <li class="contact__item">
        <span class="contact__icon">
          <svg viewBox="0 0 20 20" aria-hidden="true">
            <path d="M5.5 2.5 L8 5.5 L6.6 7.6 C7.6 9.8 9.9 12.2 12.3 13.4 L14.4 12 L17.5 14.5 L16 17 C9.5 17.5 2.5 10.5 3 4 Z" fill="var(--white)"/>
          </svg>
        </span>
        +1 628 309 4156
      </li>
      <li class="contact__item">
        <span class="contact__icon">
          <svg viewBox="0 0 20 20" aria-hidden="true" fill="none" stroke="var(--white)" stroke-width="1.3">
            <circle cx="10" cy="10" r="7.5"/>
            <ellipse cx="10" cy="10" rx="3.2" ry="7.5"/>
            <line x1="2.5" y1="10" x2="17.5" y2="10"/>
            <path d="M3.8 6.2 H16.2 M3.8 13.8 H16.2"/>
          </svg>
        </span>
        velvetharbor.com
      </li>
    </ul>
  </section>

</main>
</body>
</html>
```